Magazine Ad for the Waste Industry

We need a full page ad design that will help us introduce our new engine cooling system into the Waste market. This system helps regulate engine temperatures for large trash trucks with its advanced technology and durable. We would like this ad to make an impact and stand out from the more cluttered looking ads that are seen in trade magazines.
The project must be submitted in either InDesign or Photoshop files.

Target Market(s)

Waste Industry, Trash truck manufacturers

Industry/Entity Type

Waste Management

Font styles to use
Sans Serif

Colors
0255a3

Requirements
Must have
• The text and images attached with a more modern industrial/masculine feel.
• Our Company colors are...
• Blue (RGB 25, 76, 159)
• Gray (RGB 129, 130, 133)
• White and black as accents as needed
• SIZING
• Spread Bleed: 9.5" x 11.375"
Nice to have
• I attached two files for a font that we have used in the past. Another font we use commonly is Ariel.

```html
<!DOCTYPE html>
<html lang="en">
<head>
<meta charset="UTF-8">
<title>Advanced Electric Engine Cooling – Full Page Ad</title>
<link href="https://fonts.googleapis.com/css2?family=Exo+2:wght@300;400&family=Roboto+Condensed:wght@500;700&display=swap" rel="stylesheet">
<style>
  :root {
    --stage: #e4e7ea;
    --blue-deep: #16417f;
    --blue-brand: #194c9f;
    --blue-mid: #0a6fae;
    --blue-glow: #4aa8cf;
    --wave-light: #1f9bd0;
    --wave-dark: #0f4f8f;
    --white: #ffffff;
    --rule: rgba(255,255,255,0.85);
    --gray: #818285;
  }
  html, body {
    margin: 0;
    width: 1200px;
    height: 1200px;
    overflow: hidden;
    background: var(--stage);
  }
  .ad {
    position: absolute;
    left: 150px;
    top: 62px;
    width: 900px;
    height: 1076px;
    overflow: hidden;
    background:
      radial-gradient(ellipse 520px 420px at 420px 500px, var(--blue-glow) 0%, rgba(74,168,207,0) 100%),
      linear-gradient(180deg, #3f6f9e 0%, var(--blue-mid) 40%, var(--blue-deep) 100%);
    color: var(--white);
  }
  .waves { position: absolute; left: 0; top: 0; width: 900px; height: 1076px; }
  .headline {
    position: absolute;
    top: 70px; left: 0; width: 100%;
    margin: 0;
    text-align: center;
    font-family: "Exo 2", sans-serif;
    font-weight: 300;
    font-size: 66px;
    line-height: 1.02;
    letter-spacing: 0.5px;
  }
  .url-block { position: absolute; top: 232px; left: 200px; width: 500px; text-align: center; }
  .url-block .rule { height: 2px; background: linear-gradient(90deg, rgba(255,255,255,0), var(--rule), rgba(255,255,255,0)); }
  .url {
    font-family: "Roboto Condensed", sans-serif;
    font-weight: 700;
    font-size: 32px;
    padding: 14px 0 16px;
  }
  .features { position: absolute; top: 320px; right: 60px; width: 420px; margin: 0; padding: 0; list-style: none; }
  .feature {
    font-family: "Roboto Condensed", sans-serif;
    font-weight: 500;
    font-size: 31px;
    line-height: 1.22;
    text-align: right;
    padding: 22px 0 20px;
    border-bottom: 2px solid;
    border-image: linear-gradient(90deg, rgba(255,255,255,0), var(--rule)) 1;
  }
  .feature:last-child { border-bottom: none; }
  .product {
    position: absolute;
    left: 120px; top: 470px;
    width: 330px; height: 340px;
    background: linear-gradient(135deg, #3a3d42 0%, #1b1c1f 70%, #2a2c30 100%);
    transform: rotate(-6deg) skewY(4deg);
    box-shadow: 10px 12px 24px rgba(0,0,0,0.35);
  }
  .brands { position: absolute; left: 230px; top: 950px; display: flex; align-items: center; gap: 50px; }
  .brand {
    font-family: "Roboto Condensed", sans-serif;
    font-weight: 700;
    font-size: 34px;
    color: var(--white);
    display: flex; align-items: center; gap: 12px;
  }
  .brand .dot { width: 44px; height: 44px; border-radius: 50%; background: var(--white); opacity: 0.85; }
  .brand.company { font-size: 56px; letter-spacing: 1px; }
</style>
</head>
<body>
  <div class="ad">
    <svg class="waves" viewBox="0 0 900 1076" aria-hidden="true">
      <path d="M0 640 C250 690 560 800 900 1000 L900 1076 L0 1076 Z" fill="var(--wave-dark)" opacity="0.55"/>
      <path d="M0 700 C260 740 560 840 900 1040" stroke="var(--wave-light)" stroke-width="26" fill="none" opacity="0.8"/>
      <path d="M0 760 C270 800 570 890 900 1076" stroke="var(--wave-dark)" stroke-width="30" fill="none" opacity="0.9"/>
      <path d="M0 820 C280 860 580 950 860 1076" stroke="var(--wave-light)" stroke-width="18" fill="none" opacity="0.6"/>
      <path d="M0 880 C260 920 520 1000 720 1076" stroke="var(--wave-dark)" stroke-width="40" fill="none" opacity="0.8"/>
    </svg>

    <h1 class="headline">ADVANCED ELECTRIC<br>ENGINE COOLING</h1>

    <div class="url-block">
      <div class="rule"></div>
      <div class="url">www.corvanthermal.com/refuse</div>
      <div class="rule"></div>
    </div>

    <ul class="features">
      <li class="feature">Fully<br>Reversible Fans</li>
      <li class="feature">Eliminate Preventative<br>Maintenance</li>
      <li class="feature">Average 8%<br>Fuel Economy</li>
      <li class="feature">Quieter Residential<br>Operation</li>
      <li class="feature">Increased<br>Horsepower</li>
    </ul>

    <div class="product" role="img" aria-label="Product photo of a black electric cooling module with four fans"></div>

    <div class="brands">
      <div class="brand product-line"><span class="dot"></span>DUALCOOL</div>
      <div class="brand company">CORVAN</div>
    </div>
  </div>
</body>
</html>
```